Valdrenix is a medical device company that needs a new look for their Packaging Design

Valdrenix is a medical device company that needs a new look for their packaging design. It should look clean and sophisticated. The logo must not be changed. Please maintain the branding of the logo.

You may refer to the attachments for our logo and the packaging template we want designed.

Industry/Entity Type

It Company

```html
<!DOCTYPE html>
<html lang="en">
<head>
<meta charset="utf-8">
<title>Valdrenix Hydrophobic Acrylic Intraocular Lens – Packaging</title>
<link href="https://fonts.googleapis.com/css2?family=Open+Sans:wght@400;600;700&family=Titillium+Web:ital,wght@1,700&display=swap" rel="stylesheet">
<style>
  :root {
    --brand-blue: #1a6db8;
    --brand-blue-light: #d9e9f6;
    --stripe-blue: #e6f0f9;
    --ink: #4a4d52;
    --ink-soft: #6b6f75;
    --paper: #ffffff;
    --stage: #efefef;
  }
  * { box-sizing: border-box; margin: 0; padding: 0; }
  html, body { width: 1200px; height: 1200px; overflow: hidden; }
  body {
    background: var(--stage);
    font-family: "Open Sans", Arial, sans-serif;
    color: var(--ink);
    position: relative;
  }
  .panel {
    position: absolute;
    left: 100px;
    width: 1000px;
    background: var(--paper);
    box-shadow: 0 2px 10px rgba(0,0,0,.08);
    overflow: hidden;
  }
  .panel--front { top: 40px; height: 570px;
    background: linear-gradient(120deg, var(--paper) 0%, var(--stripe-blue) 55%, var(--paper) 100%); }
  .panel--back { top: 630px; height: 540px;
    background: linear-gradient(120deg, var(--paper) 0%, var(--stripe-blue) 60%, var(--paper) 100%); }

  .brand-band {
    position: absolute; left: 0; right: 0;
    background: var(--brand-blue);
    display: flex; align-items: center;
  }
  .panel--front .brand-band { top: 50px; height: 120px; padding-left: 100px; }
  .wordmark {
    font-family: "Open Sans", Arial, sans-serif;
    font-weight: 400;
    color: var(--paper);
    display: flex; align-items: center; gap: 14px;
    letter-spacing: 1px;
  }
  .panel--front .wordmark { font-size: 62px; }
  .wordmark__dot { width: 18px; height: 18px; border-radius: 50%; background: var(--paper); }

  .product-name {
    position: absolute; left: 100px; top: 200px;
    font-size: 40px; font-weight: 700; line-height: 1.2; color: var(--ink);
  }
  .lens-art {
    position: absolute; left: 560px; top: 20px; width: 330px; height: 490px;
    border-radius: 50%;
    background: radial-gradient(ellipse at 45% 45%, #f4f9fd 0%, #cfe3f3 55%, #b9d5ec 100%);
    opacity: .9;
  }
  .tagline-script {
    position: absolute; left: 60px; top: 392px;
    font-family: "Titillium Web", Arial, sans-serif;
    font-style: italic; font-weight: 700;
    font-size: 60px; line-height: 80px; color: var(--brand-blue);
  }
  .edge-band {
    position: absolute; left: 0; right: 0; bottom: 30px; height: 60px;
    background: var(--brand-blue);
    color: var(--paper);
    font-weight: 600; font-size: 26px;
    display: flex; align-items: center; padding-left: 60px;
    letter-spacing: .5px;
  }

  /* back panel */
  .back-header {
    position: absolute; left: 0; right: 0; top: 0; height: 70px;
    background: var(--brand-blue);
    display: flex; align-items: center; justify-content: space-between;
    padding: 0 40px;
  }
  .panel--back .wordmark { font-size: 32px; gap: 10px; }
  .panel--back .wordmark__dot { width: 12px; height: 12px; }
  .back-header__line { color: var(--paper); font-weight: 600; font-size: 16px; }
  .lens-outline {
    position: absolute; left: 60px; top: 110px; width: 230px; height: 340px;
    border-radius: 50%;
    background: linear-gradient(160deg, var(--brand-blue-light), #eef5fb);
  }
  .notice {
    position: absolute; left: 360px; top: 88px; width: 560px;
    font-size: 11.5px; line-height: 1.3; color: var(--ink);
  }
  .notice p { margin-bottom: 4px; }
  .symbols {
    position: absolute; left: 360px; bottom: 18px; height: 26px;
    display: flex; gap: 22px; align-items: center;
  }
  .symbols svg { display: block; }
  .sterile-mark {
    display: flex; border: 1.5px solid var(--ink); font-size: 10px; font-weight: 700; line-height: 1.4;
  }
  .sterile-mark span { padding: 2px 5px; }
  .sterile-mark span + span { border-left: 1.5px solid var(--ink); }
</style>
</head>
<body>

<section class="panel panel--front" aria-label="Front panel">
  <div class="lens-art" role="img" aria-label="Illustration of an intraocular lens with two curved haptics"></div>
  <div class="brand-band">
    <div class="wordmark">Valdrenix<span class="wordmark__dot"></span></div>
  </div>
  <h1 class="product-name">Hydrophobic Acrylic<br>Intraocular Lens</h1>
  <div class="tagline-script">Aspheric</div>
  <div class="edge-band">WITH 360° SQUARE EDGE</div>
</section>

<section class="panel panel--back" aria-label="Back panel">
  <div class="back-header">
    <div class="wordmark">Valdrenix<span class="wordmark__dot"></span></div>
    <div class="back-header__line">WITH 360° SQUARE EDGE · Hydrophobic Acrylic Intraocular Lens</div>
  </div>
  <div class="lens-outline" role="img" aria-label="Dashed outline drawing of the intraocular lens"></div>
  <div class="notice">
    <p>Contains one sterile intraocular lens<br>Do not use if the packaging is damaged<br>Do not resterilize</p>
    <p>Bevat één steriele intraoculaire lens<br>Niet gebruiken als de verpakking beschadigd is<br>Niet opnieuw steriliseren</p>
    <p>Contient une lentille intraoculaire stérile<br>Ne pas utiliser si l'emballage est endommagé<br>Ne pas restériliser</p>
    <p>Enthält eine sterile intraokulare Linse<br>Nicht verwenden, wenn die Verpackung beschädigt ist<br>Nicht resterilisieren</p>
    <p>Περιέχει ένα αποστειρωμένο ενδοφθάλμιο φακό<br>Μην το χρησιμοποιείτε εάν η συσκευασία έχει υποστεί ζημιά<br>Μην επαναποστειρώνετε</p>
    <p>Contiene una lente intraoculare sterile<br>Non usare se la confezione è danneggiata<br>Non risterilizzare</p>
    <p>Contém uma lente intra-ocular esterilizada<br>Não use se a embalagem está danificada<br>Não reesterilize</p>
    <p>Contiene una lente intraocular estéril<br>No utilizar si el envase está dañado<br>No vuelva a esterilizar</p>
  </div>
  <div class="symbols">
    <div class="sterile-mark"><span>STERILE</span><span>EO</span></div>
    <svg width="26" height="24" viewBox="0 0 26 24" aria-label="Caution"><path d="M13 2 L24 22 H2 Z" fill="none" stroke="#4a4d52" stroke-width="2"/><line x1="13" y1="9" x2="13" y2="15" stroke="#4a4d52" stroke-width="2"/><circle cx="13" cy="18.5" r="1.2" fill="#4a4d52"/></svg>
    <svg width="24" height="24" viewBox="0 0 24 24" aria-label="Do not reuse"><circle cx="12" cy="12" r="10" fill="none" stroke="#4a4d52" stroke-width="2"/><text x="12" y="16" text-anchor="middle" font-size="11" font-family="Open Sans, sans-serif" fill="#4a4d52">2</text><line x1="5" y1="5" x2="19" y2="19" stroke="#4a4d52" stroke-width="2"/></svg>
    <svg width="24" height="24" viewBox="0 0 24 24" aria-label="Do not resterilize"><circle cx="12" cy="12" r="10" fill="none" stroke="#4a4d52" stroke-width="2"/><rect x="7" y="9" width="10" height="6" fill="none" stroke="#4a4d52" stroke-width="1.5"/><line x1="5" y1="5" x2="19" y2="19" stroke="#4a4d52" stroke-width="2"/></svg>
  </div>
</section>

</body>
</html>
```